Identification Supplier website

Front and product page designs required for this Business Catalyst website for an identification supply company.

Also interested in coding same into finished site for additional fee.

Client is a security/event ID supplies company selling identification products like card holders, printers, lanyards, clips and so on.

Current placeholder site is at:
http://www.markovatel.com.au/

Other sites the client likes are at:

www.brantovagoods.com.au

www.tagwarely.com.au

www.rvb.com.au

http://start42.veldrana.co.nz/online/welcome.csn

Otherwise colour scheme should follow logo and structure should follow wireframe attached.

```html
<!DOCTYPE html>
<html lang="en">
<head>
<meta charset="utf-8">
<title>Markovatel – ID Systems, Supplies, Services and Accessories</title>
<link rel="stylesheet" href="https://fonts.googleapis.com/css2?family=Oswald:wght@400;500&family=Arimo:wght@400;700&display=swap">
<style>
:root{
  --navy:#1e3a5f;
  --navy-deep:#17304f;
  --sky:#1793d2;
  --sky-light:#2aa3df;
  --cyan-text:#7fd4f5;
  --ink:#1b1b1b;
  --grey-text:#555;
  --line:#d2d2d2;
  --orange:#f7941d;
  --white:#fff;
}
*{box-sizing:border-box;margin:0;padding:0}
html,body{width:1200px;height:1134px;overflow:hidden}
body{position:relative;background:radial-gradient(ellipse at 50% 45%,#ffffff 0%,#f1f1f1 55%,#e2e2e2 100%);font-family:"Arimo",Arial,sans-serif;color:var(--ink)}
.abs{position:absolute}
.top-rule{left:0;top:0;width:1200px;height:3px;background:var(--navy)}
.header{left:0;top:3px;width:1200px;height:97px;background:linear-gradient(#fafafa,#ececec)}
.brand{left:200px;top:28px}
.brand-name{font-family:"Arimo",Arial,sans-serif;font-size:34px;color:var(--navy);font-weight:400;line-height:1;display:flex;align-items:center;gap:8px}
.brand-dot{width:14px;height:14px;border-radius:50%;background:var(--sky)}
.brand-tag{font-size:8.5px;color:#7a8a9a;margin-top:8px;margin-left:52px;white-space:nowrap}
.header-sep{left:476px;top:26px;width:1px;height:54px;background:#d0d0d0;box-shadow:1px 0 0 #fff}
.nav{left:505px;top:52px;width:495px;height:26px;border-bottom:3px solid var(--line);display:flex;justify-content:space-between;white-space:nowrap}
.nav a{font-family:"Oswald",sans-serif;font-size:15px;line-height:20px;color:var(--ink);text-decoration:none;padding:0 11px;position:relative;white-space:nowrap}
.nav a:last-child{padding-right:10px}
.nav a.current{color:var(--sky)}
.nav a.current::after{content:"";position:absolute;left:0;right:0;bottom:-5px;height:3px;background:var(--sky)}
.band{left:0;top:100px;width:1200px;height:294px;background:var(--sky)}
.hero{left:200px;top:106px;width:596px;height:281px;background:radial-gradient(ellipse at 65% 40%,#8fa7ff 0%,#3a4fd6 35%,#1a2a9e 70%,#101a6a 100%)}
.hero-title{left:196px;top:188px;width:256px;height:130px;background:rgba(10,14,28,.88);padding:6px 0 0 15px;font-family:"Oswald",sans-serif;white-space:nowrap;overflow:hidden}
.hero-title div{line-height:1}
.hero-title .l1{font-size:40px;height:43px;color:var(--cyan-text);font-weight:500}
.hero-title .l2{font-size:24px;height:25px;color:var(--sky)}
.hero-title .l3{font-size:47px;color:var(--white);font-weight:500;letter-spacing:-.3px}
.news{left:813px;top:110px;width:190px}
.news h2{font-family:"Oswald",sans-serif;font-weight:500;font-size:22px;color:var(--navy);margin-bottom:6px}
.news ul{list-style:none}
.news li{font-size:9.4px;font-weight:700;color:var(--white);line-height:11.5px;padding-left:15px;position:relative;margin-bottom:7px}
.news li::before{content:"";position:absolute;left:2px;top:4px;width:4px;height:4px;border-radius:50%;background:var(--navy)}
.tile{width:188px;height:188px;border:3px solid #e6e6e6;overflow:hidden}
.tile .photo{position:absolute;inset:0}
.tile .cap{position:absolute;left:0;right:0;bottom:0;height:36px;background:rgba(40,40,40,.82);font-family:"Oswald",sans-serif;font-size:17px;color:var(--white);padding:4px 0 0 8px;white-space:nowrap}
.tile .plus{position:absolute;right:0;bottom:0;width:30px;height:30px}
.newsletter{left:813px;top:407px;width:188px;height:104px;background:linear-gradient(#2c6e9f,#1d4a78)}
.newsletter h3{position:absolute;left:55px;top:11px;font-family:"Oswald",sans-serif;font-weight:500;font-size:18px;color:var(--white)}
.newsletter .mail-icon{position:absolute;left:10px;top:6px}
.newsletter .email{position:absolute;left:7px;top:38px;width:174px;height:25px;background:var(--white);border:1px solid #ccc;font-size:9px;color:#c4c4c4;padding:7px 0 0 7px}
.newsletter .subscribe{position:absolute;left:92px;top:70px;width:87px;height:25px;background:var(--orange);color:var(--white);font-size:13px;text-align:center;line-height:25px}
.featured{left:813px;top:527px;width:188px;height:297px;background:var(--white);box-shadow:0 0 3px rgba(0,0,0,.1)}
.featured h3{height:37px;background:linear-gradient(#2c6e9f,#1d4a78);font-family:"Oswald",sans-serif;font-weight:500;font-size:21px;color:var(--white);padding:3px 0 0 12px;white-space:nowrap}
.featured .shot{position:absolute;left:12px;top:46px;width:162px;height:136px;border:3px solid #e6e6e6;background:radial-gradient(ellipse at 50% 55%,#4fb3e6 0%,#cfe9f5 45%,#fff 75%)}
.featured h4{position:absolute;left:12px;top:189px;font-family:"Oswald",sans-serif;font-weight:500;font-size:16px;color:var(--navy)}
.featured p{position:absolute;left:12px;top:213px;width:154px;font-size:9.3px;line-height:11.6px;color:#333}
.footer{left:0;top:1021px;width:1200px;height:113px;background:var(--navy)}
.foot-brand{left:200px;top:1041px;font-size:28px;color:#4d6788;display:flex;align-items:center;gap:7px}
.foot-brand .brand-dot{width:12px;height:12px;background:#4d6788}
.foot-legal{left:197px;top:1085px;font-size:9px;color:#8195ad;line-height:14px;letter-spacing:.2px}
.vsep{top:1037px;width:1px;height:75px;border-left:1px dashed #4b6585}
.contact{left:482px;top:1044px;font-size:9px;color:#cfd9e4;line-height:13.5px;letter-spacing:.3px;white-space:nowrap}
.links-title{left:790px;top:1032px;font-family:"Oswald",sans-serif;font-size:21px;color:var(--sky-light)}
.links{top:1072px;font-size:9.4px;color:#cfd9e4;line-height:13px;list-style:none;white-space:nowrap}
</style>
</head>
<body>
<div class="abs top-rule"></div>
<header class="abs header"></header>
<div class="abs brand">
  <div class="brand-name"><span class="brand-dot"></span>Markovatel</div>
  <div class="brand-tag">ID Systems, Supplies, Services and Accessories</div>
</div>
<div class="abs header-sep"></div>
<nav class="abs nav">
  <a class="current" href="#">HOME</a><a href="#">PRODUCTS</a><a href="#">SERVICES</a><a href="#">FEATURES</a><a href="#">HOW IT WORKS</a><a href="#">CONTACT US</a>
</nav>

<div class="abs band"></div>
<div class="abs hero" role="img" aria-label="Blue fingerprint over circuit lines"></div>
<div class="abs hero-title">
  <div class="l1">EVERYTHING</div>
  <div class="l2">YOU WILL EVER NEED IN</div>
  <div class="l3">ID SUPPLIES</div>
</div>
<section class="abs news">
  <h2>WHAT'S NEW?</h2>
  <ul>
    <li>Duis lacinia elit non ipsum fermentum andit.</li>
    <li>Pellentesque suscipit dignissim diam, eget tincidunt magna pharetra vel.</li>
    <li>Morbi ut nisl non ipsum rutrum hendrerit vitae et felis.</li>
    <li>Donec ac sem sit amet metus sagittis rhoncus.</li>
    <li>Maecenas porta felis quis ante lobortis dignissim.</li>
    <li>Mauris iaculis magna vitae metus pharetra lobortis.</li>
    <li>Morbi ut nisl non ipsum rutrum hendrerit vitae et felis.</li>
    <li>Donec ac sem sit amet metus sagittis rhoncus.</li>
  </ul>
</section>

<svg width="0" height="0" style="position:absolute">
  <defs>
    <symbol id="corner-plus" viewBox="0 0 30 30">
      <polygon points="30,0 30,30 0,30" fill="#1793d2"/>
      <path d="M15 22h10M20 17v10" stroke="#fff" stroke-width="2"/>
    </symbol>
  </defs>
</svg>

<div class="abs tile" style="left:200px;top:407px"><div class="photo" role="img" aria-label="Card printer with ribbon" style="background:radial-gradient(circle at 55% 45%,#3ab2dc 0%,#d9eef6 50%,#fff 80%)"></div><div class="cap">Card Printers &amp; Ribbons</div><svg class="plus"><use href="#corner-plus"/></svg></div>
<div class="abs tile" style="left:404px;top:407px"><div class="photo" role="img" aria-label="Life ring against blue sky" style="background:radial-gradient(circle at 45% 35%,#f3f3f3 0%,#e8585a 25%,#2c63c4 45%,#153a9a 100%)"></div><div class="cap">Solutions</div><svg class="plus"><use href="#corner-plus"/></svg></div>
<div class="abs tile" style="left:608px;top:407px"><div class="photo" role="img" aria-label="Hand holding a card" style="background:linear-gradient(160deg,#8a1e28 0%,#3c3f58 40%,#9fb0c4 100%)"></div><div class="cap">Bureau Services</div><svg class="plus"><use href="#corner-plus"/></svg></div>
<div class="abs tile" style="left:200px;top:611px"><div class="photo" role="img" aria-label="Laminating machine" style="background:linear-gradient(#dcdcdc,#f5f5f5 50%,#c9c9c9)"></div><div class="cap">Laminates</div><svg class="plus"><use href="#corner-plus"/></svg></div>
<div class="abs tile" style="left:404px;top:611px;border-top-color:var(--navy)"><div class="photo" role="img" aria-label="Assorted printed lanyards" style="background:linear-gradient(135deg,#fff 20%,#2b5fa8 40%,#3aa36a 55%,#e86f2a 70%,#fff 90%)"></div><div class="cap">Lanyards</div><svg class="plus"><use href="#corner-plus"/></svg></div>
<div class="abs tile" style="left:608px;top:611px"><div class="photo" role="img" aria-label="Coloured silicone wristbands" style="background:linear-gradient(120deg,#fff 10%,#2a5bd6 30%,#e0262e 50%,#3cc43c 70%,#fff 90%)"></div><div class="cap">Wristbands</div><svg class="plus"><use href="#corner-plus"/></svg></div>
<div class="abs tile" style="left:200px;top:815px"><div class="photo" role="img" aria-label="Coloured card holders" style="background:linear-gradient(90deg,#f2f2f2 20%,#e0256a 35%,#c2185b 65%,#1d1d1d 80%)"></div><div class="cap">Cardholders</div><svg class="plus"><use href="#corner-plus"/></svg></div>
<div class="abs tile" style="left:404px;top:815px"><div class="photo" role="img" aria-label="ID accessories: reels, badge holders, ribbon" style="background:radial-gradient(circle at 50% 50%,#fff 40%,#eaeaea 100%)"></div><div class="cap">Accessories</div><svg class="plus"><use href="#corner-plus"/></svg></div>

<aside class="abs newsletter">
  <svg class="mail-icon" width="38" height="30" viewBox="0 0 38 30"><rect x="2" y="8" width="32" height="20" fill="#fff"/><path d="M2 8l16 12 16-12" fill="none" stroke="#bbb"/><circle cx="18" cy="10" r="8" fill="#3aa84a"/><text x="18" y="14" font-size="11" fill="#fff" text-anchor="middle" font-family="Arimo,sans-serif">@</text></svg>
  <h3>NEWSLETTER</h3>
  <div class="email">Enter your Email Address ...</div>
  <div class="subscribe">Subscribe</div>
</aside>

<aside class="abs featured">
  <h3>FEATURED PRODUCT</h3>
  <div class="shot" role="img" aria-label="Compact card printer"></div>
  <h4>Consectrue Ejrhe</h4>
  <p>Lorem ipsum dolor sit amet, consectetuer adipiscing elit, sed diam nonummy nibh euismod tincidunt ut laoreet dolore magna aliquam erat volutpat. Ut wisi enim ad minim veniam.</p>
</aside>

<footer class="abs footer"></footer>
<div class="abs foot-brand"><span class="brand-dot"></span>Markovatel</div>
<div class="abs foot-legal">Copyright © 2013. Markovatel. All Rights Reserved.<br>Privacy Policy &nbsp;|&nbsp; Terms &amp; Conditions</div>
<div class="abs vsep" style="left:448px"></div>
<address class="abs contact" style="font-style:normal">
  88/12 Harlow Crescent, Brenton Vale, Victoria, 3188 Australia<br>
  Phone: (03)9000 1427<br>
  Fax: (03)9000 1428<br>
  E-mail: admin@markovatel.com.au<br>
  E-mail: sales@markovatel.com.au
</address>
<div class="abs vsep" style="left:754px"></div>
<div class="abs links-title">SITE LINKS</div>
<ul class="abs links" style="left:790px"><li>Home</li><li>Products</li><li>Services</li></ul>
<ul class="abs links" style="left:880px;top:1071px"><li>Features</li><li>How It Works</li><li>Contact Us</li></ul>
</body>
</html>
```